1 page Venture SpokeWell Investor Sheet. This is given to individuals as well as corporations

we are focusing on the "Slip Sheet" (or) "Investor
Sheet'. We will be using this one page document to introduce folks to our organization and open conversations on monetary donations. Must have an ask for $50 to sponsor a child.

Some of the things we are looking for are the overall style/design.
Content should include...

1) Overall: Who we are, What we do, Why or How we do it (I also am
including a copy of our Mission and values statement)

2) Our ask - via the missing link (or) $50 to sponsor a child...How can I help?

3) Maybe a testimonial or two

4) Metrics / Statistics from our programs (may pull some of this from annual report for now)

Target Market(s)

Individual and Corporate

Industry/Entity Type

Non-Profit

Font styles to use
Other font styles liked:
• please use style guide for correct fonts

Requirements
Must have
• 1) Overall: Who we are, What we do, Why or How we do it (I also am including a copy of our Mission and values statement)
• 2) Our ask – via the missing link (or) $50 to sponsor a child…How can I help?
• 3) Maybe a testimonial or two
• 4) Metrics / Statistics from our programs (may pull some of this from annual report for now)
• 5) logo
• 6) photos of kids on bikes
• 7) our color scheme and fonts per style guideline

```html
<!DOCTYPE html>
<html lang="en">
<head>
<meta charset="utf-8">
<title>Venture SpokeWell – Investor Sheet</title>
<link href="https://fonts.googleapis.com/css2?family=Sniglet:wght@400;800&family=PT+Sans:wght@400;700&display=swap" rel="stylesheet">
<style>
  :root{
    --ink:#1d1a17;
    --teal:#3fc3dc;
    --orange:#f28227;
    --lime:#bcd631;
    --sky:#45c4de;
    --paper:#ffffff;
    --text:#222;
  }
  *{box-sizing:border-box;margin:0;padding:0}
  html,body{width:1200px;height:1200px;overflow:hidden;background:#fff}
  body{position:relative;font-family:"PT Sans",sans-serif;color:var(--text)}
  .sheet{position:absolute;background:var(--paper);overflow:hidden;box-shadow:8px 10px 14px rgba(0,0,0,.35)}
  .sheet--about{left:74px;top:243px;width:428px;height:603px}
  .sheet--help{left:591px;top:211px;width:473px;height:667px}

  .masthead{position:absolute;left:0;top:0;width:100%;background:var(--ink)}
  .sheet--about .masthead{height:73px}
  .sheet--help .masthead{height:81px}
  .brand{position:absolute;left:10px;display:flex;align-items:center;gap:5px;
    font-family:"Sniglet",sans-serif;font-size:11px;color:var(--teal);line-height:1}
  .sheet--about .brand{top:30px}
  .sheet--help .brand{top:34px}
  .brand__dot{width:12px;height:12px;border-radius:50%;background:var(--orange)}
  .tagline{position:absolute;right:6px;font-family:"Sniglet",sans-serif;font-size:16.5px;color:var(--teal);white-space:nowrap;letter-spacing:.2px}
  .sheet--about .tagline{top:12px}
  .sheet--help .tagline{top:13px}
  .social{position:absolute;right:7px;display:flex;gap:8px}
  .sheet--about .social{top:40px}
  .sheet--help .social{top:45px}
  .social span{width:16px;height:16px;border-radius:2px;background:var(--orange)}

  .photo{position:absolute;left:0;width:100%}
  .photo--riders{top:73px;height:162px;background:linear-gradient(180deg,#8fa86a 0%,#6f8c4a 45%,#9a8a78 75%,#5c5a58 100%)}
  .photo--group{top:426px;height:203px;background:linear-gradient(180deg,#b99a86 0%,#8d6f63 35%,#4f6d8f 70%,#7c7a74 100%)}

  .heading{position:absolute;left:0;width:100%;text-align:center;font-family:"Sniglet",sans-serif;color:var(--orange);font-size:19px}
  .sheet--about .heading{top:246px;padding-left:10px}
  .sheet--help .heading{top:94px;font-size:20px}

  .copy{position:absolute;font-size:7.5px;line-height:1.38;color:var(--text)}
  .copy p{margin-bottom:7px}
  .sheet--about .copy{left:10px;top:281px;width:412px}
  .sheet--help .copy{left:16px;top:138px;width:448px;font-size:8px}
  .sheet--help .copy p{margin-bottom:8px}

  .pledge{position:absolute;left:52px;top:205px;width:358px;font-size:8px}
  .pledge__head{background:var(--orange);color:#fff;font-family:"Sniglet",sans-serif;font-size:12.5px;text-align:center;height:19px;line-height:19px}
  .pledge__options{background:var(--lime);padding:2px 0 3px 66px}
  .pledge__option{display:flex;align-items:center;gap:6px;height:16px}
  .tick{width:9px;height:9px}
  .pledge__field{background:var(--sky);height:16.5px;line-height:16.5px;padding-left:3px;border-bottom:1px solid #2b8fa4}

  .actions{position:absolute;top:371px;left:243px;display:flex;gap:34px}
  .btn{height:26px;border-radius:8px;background:var(--orange);color:#fde6cf;font-family:"Sniglet",sans-serif;font-size:12.5px;line-height:26px;text-align:center}
  .btn--clear{width:55px}
  .btn--donate{width:78px}
  .disclaimer{position:absolute;left:11px;top:408px;font-size:8px;white-space:nowrap}

  .footer{position:absolute;left:0;bottom:0;width:100%;background:var(--lime);border-bottom:3px solid var(--ink);text-align:center;font-size:7.6px;color:var(--ink)}
  .sheet--about .footer{height:38px;padding-top:21px}
  .sheet--help .footer{height:38px;padding-top:12px;font-size:8.2px}
</style>
</head>
<body>

<section class="sheet sheet--about">
  <header class="masthead">
    <div class="brand"><span class="brand__dot"></span>Venture SpokeWell</div>
    <div class="tagline">Denver CO Charity Devoted to Kids &amp; Families</div>
    <div class="social"><span></span><span></span><span></span></div>
  </header>
  <div class="photo photo--riders" role="img" aria-label="Four children riding bicycles along a grassy country path"></div>
  <h2 class="heading">What is Venture SpokeWell?</h2>
  <div class="copy">
    <p>Venture SpokeWell is a Douglas County based 501(c)3 Non-Profit. We recycle used bikes, fix them up and provide them to those in need.</p>
    <p>Venture SpokeWell was founded in 2010 to provide smiles to children all over Colorado via a bicycle. That has not changed today. Our first run at this venture led us to create a program that would not only guarantee smiles but would also influence children's academic behavior in a positive manner. As part of our Pedal Promise Program,</p>
    <p>Children, during their academic year, are encouraged to earn a bike by improving in 3 areas; Respect, Attendance and Academic Growth.</p>
    <p>Venture SpokeWell works with multiple agencies to provide stability for children. The gifted bicycle becomes a constant in a life of change. Venture SpokeWell collects bicycles from participating locations on a weekly basis. Bikes are brought back to the repair shop and inspected. If a bike cannot be fixed for reuse, it is dismantled. Each reusable part is salvage for future use. All remaining bike parts are then recycled.</p>
    <p>Venture SpokeWell has become very good at recycling bicycles from the community and through our Pedal Promise Program, the children have achieved an 89% success rate of excelling in attendance, grades and respect to earn these bicycles.</p>
    <p>However, the financial gap to fill the need of safe bicycles for these kids is growing.</p>
    <p>Each year, Venture SpokeWell reaches out to the community to raise the funds necessary to help over 1,500 children strive for success. It is our commitment to keep our costs low and opportunities for children high, and that is where we need your help.</p>
  </div>
  <footer class="footer">spokewell.org | 844-555-0142 | 410 Alder Ridge Rd. Suite 12 Maple Fork, CO 80100| hello@spokewell.org</footer>
</section>

<section class="sheet sheet--help">
  <header class="masthead">
    <div class="brand"><span class="brand__dot"></span>Venture SpokeWell</div>
    <div class="tagline">Denver CO Charity Devoted to Kids &amp; Families</div>
    <div class="social"><span></span><span></span><span></span></div>
  </header>
  <h2 class="heading">How can You help?</h2>
  <div class="copy">
    <p>A $50 sponsorship provides a child with a bicycle, helmet, lock, and the opportunity to achieve success and gain confidence in their abilities.</p>
    <p>We envision a world where every child experiences the joy and freedom associated with a bicycle.</p>
    <p>You may help fill the gap by becoming a MISSING LINK donor or sponsor...</p>
  </div>
  <form class="pledge">
    <div class="pledge__head">Sponsor a child:</div>
    <div class="pledge__options">
      <div class="pledge__option"><svg class="tick" viewBox="0 0 10 10"><rect x=".5" y=".5" width="9" height="9" fill="none" stroke="#222"/><path d="M2 5l2 2.5L8.5 1" fill="none" stroke="#222" stroke-width="1.4"/></svg>$50 annual donation sponsors a child</div>
      <div class="pledge__option"><svg class="tick" viewBox="0 0 10 10"><rect x=".5" y=".5" width="9" height="9" fill="none" stroke="#222"/><path d="M2 5l2 2.5L8.5 1" fill="none" stroke="#222" stroke-width="1.4"/></svg>$50 monthly donation sponsors 12 children each year</div>
      <div class="pledge__option"><svg class="tick" viewBox="0 0 10 10"><rect x=".5" y=".5" width="9" height="9" fill="none" stroke="#222"/><path d="M2 5l2 2.5L8.5 1" fill="none" stroke="#222" stroke-width="1.4"/></svg>$Other:</div>
    </div>
    <div class="pledge__head">Sponsor a school:</div>
    <div class="pledge__options">
      <div class="pledge__option"><svg class="tick" viewBox="0 0 10 10"><rect x=".5" y=".5" width="9" height="9" fill="none" stroke="#222"/><path d="M2 5l2 2.5L8.5 1" fill="none" stroke="#222" stroke-width="1.4"/></svg>$15,000 sponsors an entire school's Pedal Promise program</div>
    </div>
    <div class="pledge__field">Name:</div>
    <div class="pledge__field">Email:</div>
    <div class="pledge__field">Phone#:</div>
  </form>
  <div class="actions">
    <div class="btn btn--clear">Clear</div>
    <div class="btn btn--donate">Donate</div>
  </div>
  <p class="disclaimer">By clicking on donate button, You agree to be contacted by Venture SpokeWell, regarding the donation.</p>
  <div class="photo photo--group" role="img" aria-label="Large group of helmeted children with their bicycles in front of a brick school building"></div>
  <footer class="footer">spokewell.org | 844-555-0142 | 410 Alder Ridge Rd. Suite 12 Maple Fork, CO 80100| hello@spokewell.org</footer>
</section>

</body>
</html>
```